Ad Banner for knowledge management portal - Promote Knowledge Submission

This banner is used in knowledge management web site.

1. Banner size: 940x380
2. Business background: Provides maintenance, design and engineering, construction, machinery operation, material procurement and production management services for petrochemical and refinery business
3. We would like to see designs that
- Promote the benefits of sharing "Lesson Learned".
- Use the keyword "I will do it better if I have to do it again"
- Promote employees to submit "Lesson Learned". It is a lesson learned from work, submitted using a predefined form template.
- Promote a campaign that will give out souvenir for all employees who submit "Lesson Learned"
- Has the message "Click here to learn more about Lesson Learned"

Requirements
Must have
• Must have a picture of technician examining machine or equipments (using cartoon character)
Should not have
• Should not include picture of real people in the design

```html
<!DOCTYPE html>
<html lang="en">
<head>
<meta charset="UTF-8">
<title>Lesson Learned Banner</title>
<link rel="stylesheet" href="https://fonts.googleapis.com/css2?family=Mansalva&family=Gochi+Hand&display=swap">
<style>
  :root {
    --page: #ffffff;
    --sky-deep: #0b4fc4;
    --sky-mid: #1a86e6;
    --sky-light: #37c3f0;
    --plant-tint: #4fd2e8;
    --worker-red: #d8372c;
    --worker-brown: #4a3428;
    --worker-yellow: #f4c21a;
    --pill-yellow: #ffc400;
    --cta-red: #e63a3d;
    --ink-white: #ffffff;
    --headline-stroke: #e23a3a;
  }
  * { margin: 0; padding: 0; box-sizing: border-box; }
  html, body { width: 1200px; height: 900px; overflow: hidden; background: var(--page); }
  .canvas { position: relative; width: 1200px; height: 900px; }

  .banner {
    position: absolute; left: 51px; top: 213px; width: 1107px; height: 448px;
    overflow: hidden;
  }
  .banner-backdrop {
    position: absolute; inset: 0;
    background:
      radial-gradient(ellipse at 70% 45%, var(--sky-light) 0%, rgba(55,195,240,0) 55%),
      linear-gradient(90deg, var(--plant-tint) 0%, var(--sky-mid) 35%, var(--sky-mid) 65%, var(--sky-deep) 100%);
  }
  .worker-figure {
    position: absolute; left: 14px; top: 5px; width: 242px; height: 443px;
    border-radius: 90px 90px 12px 12px;
    background: linear-gradient(180deg, var(--worker-yellow) 0%, var(--worker-yellow) 12%, var(--worker-red) 28%, var(--worker-red) 45%, var(--worker-brown) 60%, var(--worker-brown) 100%);
  }

  .headline {
    position: absolute; left: 271px; top: 46px;
    font-family: "Mansalva", cursive;
    font-weight: 400;
    color: var(--ink-white);
    -webkit-text-stroke: 1.5px var(--headline-stroke);
    paint-order: stroke fill;
    text-shadow: 2px 3px 0 rgba(160,20,30,0.55);
    line-height: 1;
    white-space: nowrap;
  }
  .headline-main { display: block; font-size: 56px; letter-spacing: 1px; }
  .headline-sub { display: block; font-size: 35px; margin-top: 6px; margin-left: -4px; }

  .pill {
    position: absolute; display: flex; align-items: center;
    height: 50px; border-radius: 25px;
    border: 3px solid var(--ink-white);
    font-family: "Gochi Hand", cursive;
    color: var(--ink-white);
    text-shadow: 1px 1px 1px rgba(120,70,0,0.5);
    white-space: nowrap;
    overflow: hidden;
    text-decoration: none;
  }
  .benefit { left: 276px; width: 328px; background: var(--pill-yellow); font-size: 20px; padding-left: 24px; gap: 18px; }
  .benefit-submit { top: 196px; }
  .benefit-souvenir { top: 263px; }
  .tick { width: 18px; height: 16px; flex: none; }

  .cta-arrow { position: absolute; left: 712px; top: 391px; width: 30px; height: 24px; }
  .cta {
    left: 745px; top: 377px; width: 328px;
    background: var(--cta-red); justify-content: center;
    font-size: 15px; padding: 0 16px;
  }
</style>
</head>
<body>
<div class="canvas">
  <section class="banner">
    <div class="banner-backdrop" role="img" aria-label="Refinery plant with circuit board and hexagon pattern in blue tones"></div>
    <div class="worker-figure" role="img" aria-label="Cartoon technician in hard hat, goggles, red shirt and overalls holding a cable"></div>

    <h1 class="headline">
      <span class="headline-main">I will do it better</span>
      <span class="headline-sub">if I have to do it again</span>
    </h1>

    <div class="pill benefit benefit-submit">
      <svg class="tick" viewBox="0 0 18 16"><path d="M2 8 L7 13 L16 2" fill="none" stroke="#fff" stroke-width="3" stroke-linecap="round" stroke-linejoin="round"/></svg>
      <span>Submit "Lesson Learned"</span>
    </div>
    <div class="pill benefit benefit-souvenir">
      <svg class="tick" viewBox="0 0 18 16"><path d="M2 8 L7 13 L16 2" fill="none" stroke="#fff" stroke-width="3" stroke-linecap="round" stroke-linejoin="round"/></svg>
      <span>Souvenir for all who submit</span>
    </div>

    <svg class="cta-arrow" viewBox="0 0 30 24"><path d="M0 8 H16 V1 L29 12 L16 23 V16 H0 Z" fill="#fff"/></svg>
    <a class="pill cta">Click here to learn more about Lesson Learned</a>
  </section>
</div>
</body>
</html>
```